Dana's Paw Spruce & Shine

I have a mobile dog grooming business and I need a design. I would like a scruffy dirty dog as a before dog. Then a clean short hair neatly groomed dog as the after been cleaned and groom by my service. Cartoon images would be good.
My services are bathing, drying, cleaning ears, clipping nails, clip and style hair and deodorising. The mobile van is white and my mobile number is 0452631084.
No dog in bath/tub designs please as they are too common.

Target Market(s)

Clients who wish their dogs to be clean and clipped, ready for the summer heat and Christmas where friends and family visit. They want their dog smelling nice and looking good.

Industry/Entity Type

Graphic Design

Contact Information for Business Card

DANA'S PAW SPRUCE & SHINE Mobile Grooming
Bath, Trim Nails, Clean Ears, Style Clip, Blow Dry,
Cologne. Call Us On: 0452631084

Font styles to use
Script

Colors
85cae6
34a6d7
0393ce
ec1f27

Requirements
Must have
• A Logo with a picture of 2 dogs.. One dirty dog, scruffy long hair, messy, neglected
• 2nd Dog, Clean, Hair neat Looking Sharp and well
• looked after.
• A comparison of two dogs the before and after shots of the same dog. Before it was groomed and after it was groomed. Cartoon form.
Nice to have
• The colour of my Van is White with a light blue stripe at the bottom. I would like colours to suit my trailer eg Grey's, Bubbles, or water drops. Red & Black writing.
• As I need business cards and vinyl sticker logo to put on my trailer.
Should not have
• No dogs in baths or tubs as they are too common in the Mobile Grooming Industry.
• Needs to be unique. .

```html
<!DOCTYPE html>
<html lang="en">
<head>
<meta charset="utf-8">
<title>Dana's Paw Spruce & Shine — Business Card</title>
<link href="https://fonts.googleapis.com/css2?family=Open+Sans:wght@400;600;700&display=swap" rel="stylesheet">
<style>
  :root {
    --page-white: #ffffff;
    --stage-grey: #b4b3b8;
    --card-white: #fbfbfb;
    --brand-blue: #5aa9dc;
    --deep-blue: #1577c4;
    --light-blue: #6cb8e6;
    --gold: #9a8153;
    --ink: #2b2b2b;
    --dog-tone: #d9d4cc;
    --dog-tone-dark: #a58a6a;
  }
  * { margin: 0; padding: 0; box-sizing: border-box; }
  html, body { width: 1200px; height: 863px; overflow: hidden; }
  body {
    font-family: "Open Sans", Arial, sans-serif;
    background: var(--page-white);
    position: relative;
  }
  .logo-strip {
    position: absolute; left: 0; top: 0; width: 1200px; height: 280px;
    display: flex; align-items: center; justify-content: center; gap: 14px;
  }
  .dog-art {
    border-radius: 10px;
  }
  .dog-art--before { background: linear-gradient(135deg, var(--dog-tone), var(--dog-tone-dark)); }
  .dog-art--after { background: linear-gradient(135deg, #f2f2f2, var(--dog-tone)); }
  .logo-strip .dog-art { width: 72px; height: 40px; }
  .logo-name {
    font-weight: 600; color: var(--brand-blue); font-size: 19px; white-space: nowrap;
  }
  .stage {
    position: absolute; left: 0; top: 280px; width: 1200px; height: 583px;
    background: var(--stage-grey);
  }
  .card {
    position: absolute; left: 290px; top: 95px; width: 620px; height: 380px;
    background: var(--card-white); border-radius: 28px; overflow: hidden;
    box-shadow: 0 14px 30px rgba(0,0,0,0.22);
  }
  .card .dog-art--before { position: absolute; left: 40px; top: 48px; width: 170px; height: 95px; }
  .card .dog-art--after { position: absolute; right: 40px; top: 120px; width: 140px; height: 110px; }
  .card-name {
    position: absolute; left: 220px; top: 70px; width: 240px;
    font-weight: 600; color: var(--brand-blue); font-size: 30px; line-height: 1.15;
  }
  .card-wave { position: absolute; left: 0; bottom: 0; width: 620px; height: 170px; }
  .contact {
    position: absolute; left: 210px; top: 190px;
  }
  .phone { font-weight: 700; color: var(--deep-blue); font-size: 26px; letter-spacing: 1px; }
  .abn { font-weight: 600; color: var(--ink); font-size: 13px; margin-top: -2px; }
  .services {
    position: absolute; left: 40px; right: 40px; bottom: 34px;
    color: #ffffff; font-size: 16px; line-height: 1.45; text-align: center;
  }
</style>
</head>
<body>
  <header class="logo-strip">
    <div class="dog-art dog-art--before" role="img" aria-label="Cartoon of a scruffy, dirty long-haired dog before grooming"></div>
    <span class="logo-name">Dana's Paw Spruce &amp; Shine</span>
    <div class="dog-art dog-art--after" role="img" aria-label="Cartoon of the same dog clean and neatly clipped after grooming"></div>
  </header>

  <main class="stage">
    <section class="card">
      <svg class="card-wave" viewBox="0 0 620 170" preserveAspectRatio="none" aria-hidden="true">
        <defs>
          <linearGradient id="bandBlue" x1="0" y1="0" x2="1" y2="0">
            <stop offset="0" stop-color="#1577c4"/>
            <stop offset="1" stop-color="#6cb8e6"/>
          </linearGradient>
        </defs>
        <path d="M0 20 C 200 40, 420 80, 620 90 L620 170 L0 170 Z" fill="url(#bandBlue)"/>
        <path d="M0 20 C 200 40, 420 80, 620 90" fill="none" stroke="#9a8153" stroke-width="3"/>
      </svg>

      <div class="dog-art dog-art--before" role="img" aria-label="Cartoon of a scruffy, dirty long-haired dog before grooming"></div>
      <h1 class="card-name">Dana's Paw Spruce &amp; Shine</h1>
      <div class="dog-art dog-art--after" role="img" aria-label="Cartoon of the same dog clean and neatly clipped after grooming"></div>

      <div class="contact">
        <p class="phone">0452631084</p>
        <p class="abn">ABN: 41 902 557 216</p>
      </div>

      <p class="services">Grooming dogs from head to tail, Bathing, Clipping, Styling, Blow Drying, Clipping nails, Cleaning ears, &amp; Flea Treatments, and Deodorising</p>
    </section>
  </main>
</body>
</html>
```